Electrical contracting business specialising in smoke detector installation needs flyer design

i need a flyer design made up highlighting the fact that the Qld legislation is changing on smoke detectors in homes for everyones safety. I am an electrical contractor ( Tandrell Electrical) specialising in smoke detector installation to comply with the new Qld legislation. Some of the wording that can be used-
When you sleep, your sense of smell also sleeps. If a fire starts, toxic fumes canovercome you. Photoelectric smoke alarms see smoke and will alert you early, so you can escape. With interconnected alarms, you will be alerted no matter where you are, or where the fire starts.
New legislation specifies the type, positioning and interconnectedness of alarms, which are critical factors for an early warning and a quick escape.
To give your family the best chance of surviving a house fire, update your smoke alarms to match the new legislation as soon as you can. Call ME on 0418362957

Target Market(s)

Body Corporates , people selling and renting their properties

Industry/Entity Type

Electrician

Colors

Designer to choose colors to be used in the design.

Requirements
Must have
• Safety aspect.

```html
<!DOCTYPE html>
<html lang="en">
<head>
<meta charset="utf-8">
<title>Smoke Alarm Legislation – Tandrell Electrical</title>
<link href="https://fonts.googleapis.com/css2?family=Open+Sans:ital,wght@0,400;0,600;0,700;0,800;1,700&family=Arvo:wght@700&display=swap" rel="stylesheet">
<style>
:root{
  --backdrop:#dcbc8c;
  --gold:#b98a3e;
  --gold-light:#d4a85a;
  --ink:#1e1e21;
  --paper:#ffffff;
  --text-light:#e9e9e9;
  --text-dark:#222;
}
*{box-sizing:border-box;margin:0;padding:0}
html,body{width:1200px;height:857px;overflow:hidden}
body{background:var(--backdrop);font-family:"Open Sans",Arial,sans-serif;position:relative}
.page{position:absolute;top:28px;width:566px;height:800px;background:var(--paper);overflow:hidden;box-shadow:0 6px 18px rgba(0,0,0,.25)}
.page--front{left:20px}
.page--back{left:614px}
.abs{position:absolute}

/* front */
.hero-photo{left:0;top:0;width:566px;height:330px;background:linear-gradient(160deg,#f6ece6 0%,#e9cfc3 45%,#f3e4de 100%)}
.brand-box{left:0;top:70px;width:190px;height:120px;background:var(--ink);border-right:3px solid var(--gold);display:flex;align-items:center;justify-content:center}
.brand-name{color:var(--gold);font-weight:600;font-size:15px;letter-spacing:.5px;text-align:center;line-height:1.25}
.headline{right:28px;top:200px;text-align:right;font-family:"Arvo",Georgia,serif;color:var(--ink);line-height:.95}
.headline .l1{font-size:40px;letter-spacing:1px}
.headline .l2{font-size:28px;letter-spacing:1px;margin-right:18px}
.intro-band{left:0;top:330px;width:566px;height:135px;background:var(--ink);border-top:4px solid var(--gold)}
.alarm-side{left:-10px;top:300px;width:170px;height:95px;border-radius:14px;background:linear-gradient(180deg,#f4f4f4 0%,#d8d8d8 55%,#4a4a4a 56%,#3a3a3a 100%)}
.intro-text{left:180px;top:350px;width:360px;color:var(--text-light);font-size:11px;line-height:1.55;text-align:center}
.glossary{left:30px;top:478px;width:345px;color:var(--text-dark);font-size:9.5px;line-height:1.4}
.glossary h2{font-size:22px;font-weight:700;color:var(--ink);margin-bottom:6px;line-height:1.3}
.glossary dt{display:inline;color:var(--gold);font-weight:700;font-size:11px}
.glossary dd{display:inline}
.glossary p{margin-bottom:3px}
.alarm-round{left:385px;top:480px;width:155px;height:105px;border-radius:50%;background:radial-gradient(circle at 40% 35%,#fafafa 0%,#e2e2e2 55%,#bdbdbd 100%)}
.footer-band{left:0;top:700px;width:566px;height:100px;background:var(--ink);border-top:4px solid var(--gold);display:flex;align-items:center;justify-content:center;text-align:center}
.footer-band p{color:var(--gold);font-weight:800;font-style:italic;font-size:19px;line-height:1.3}

/* back */
.head-band{left:0;top:0;width:566px;height:80px;background:var(--gold);display:flex;align-items:center;justify-content:center;text-align:center;border-bottom:6px solid var(--paper)}
.head-band h2,.mid-band h2{color:#fff;font-weight:800;font-size:19px;line-height:1.15;letter-spacing:.3px}
.dark-block{left:0;width:566px;background:var(--ink)}
.dark-block--upper{top:86px;height:288px}
.dark-block--lower{top:440px;height:160px}
.col{color:var(--text-light);font-size:9.2px;line-height:1.4}
.col h3{color:var(--gold-light);font-size:14px;font-weight:700;margin-bottom:5px;line-height:1.3}
.col p{margin-bottom:5px}
.col ol{list-style:none;margin-bottom:5px}
.col li{padding-left:8px}
.col-left-up{left:26px;top:98px;width:235px}
.col-right-up{left:285px;top:98px;width:262px}
.alarm-back{left:60px;top:272px;width:150px;height:75px;border-radius:14px;background:linear-gradient(180deg,#f4f4f4 0%,#d8d8d8 55%,#4a4a4a 56%,#3a3a3a 100%)}
.mid-band{left:0;top:374px;width:566px;height:66px;background:var(--gold);display:flex;align-items:center;justify-content:center;text-align:center}
.col-left-low{left:26px;top:454px;width:235px}
.col-right-low{left:285px;top:454px;width:262px}
.closing{left:40px;top:615px;width:486px;font-size:10.5px;line-height:1.5;color:var(--text-dark);text-align:center}
.call{right:30px;top:665px;font-size:22px;font-weight:800;color:var(--ink)}
.foot-brand{left:0;top:710px;width:170px;height:90px;background:var(--ink);border-top:3px solid var(--gold);display:flex;align-items:center;justify-content:center}
.foot-brand .brand-name{font-size:13px}
.web-band{left:170px;top:730px;width:396px;height:70px;background:var(--gold);display:flex;align-items:center;justify-content:flex-end;padding-right:26px}
.web-band span{color:#fff;font-weight:700;font-size:16px;letter-spacing:1px}
</style>
</head>
<body>

<section class="page page--front">
  <div class="abs hero-photo" role="img" aria-label="Photo of a woman sleeping peacefully on white pillows"></div>
  <div class="abs brand-box"><span class="brand-name">Tandrell Electrical<br>Electrical Contractor</span></div>
  <h1 class="abs headline"><span class="l1">SMOKE ALARM</span><br><span class="l2">LEGISLATION</span></h1>
  <div class="abs intro-band"></div>
  <div class="abs alarm-side" role="img" aria-label="Photo of a photoelectric smoke alarm, side view"></div>
  <p class="abs intro-text">When you sleep, your sense of smell also sleeps. If a fire starts, toxic fumes can over come you. Photo electric smoke alarms see smoke and will alert you early, so you can escape. With interconnected alarms, you will be alerted no matter where you are, or where the fire starts.</p>
  <div class="abs alarm-round" role="img" aria-label="Photo of a round white ceiling smoke alarm"></div>
  <div class="abs glossary">
    <h2>Glossary of Terms*</h2>
    <dl>
      <p><dt>Dwellings</dt> <dd>- houses, townhouses (Class 1A) and units (Class 2).</dd></p>
      <p><dt>Photoelectric</dt> <dd>- the method the device uses to detect smoke.</dd></p>
      <p><dt>Hardwired</dt> <dd>- connected to the domestic dwelling's electricity supply.</dd></p>
      <p><dt>Interconnected</dt> <dd>- if one smoke alarm sounds all the other smoke alarms will also sound. Interconnection can be wired or wireless.</dd></p>
      <p><dt>Substantial</dt> <dd>- work carried out under a building development approval or the total building works equals 50% of the dwelling over 3 years.</dd></p>
      <p><dt>Storey</dt> <dd>- a space within a building which is situated between one floor level and the floor level or roof above.</dd></p>
    </dl>
  </div>
  <div class="abs footer-band"><p>Smoke alarms must be either hardwired or powered<br>by a nonremovable 10-year battery.</p></div>
</section>

<section class="page page--back">
  <div class="abs head-band"><h2>DWELLINGS BEING SOLD, LEASED OR AN<br>EXISTING LEASE IS RENEWED</h2></div>
  <div class="abs dark-block dark-block--upper"></div>
  <div class="abs col col-left-up">
    <h3>From 1 January 2017</h3>
    <p>Requirements as for existing dwellings.</p>
    <p>Existing landlord's and tenant's obligations regarding the installation and testing of smoke alarms continue.</p>
    <p>Property sellers must continue to lodge a Form 24 with the Queensland Land Registry Office stating the requirements of the smoke alarm legislation have been met.</p>
  </div>
  <div class="abs alarm-back" role="img" aria-label="Photo of a photoelectric smoke alarm"></div>
  <div class="abs col col-right-up">
    <h3>From 1 January 2022</h3>
    <p>Smoke alarms in the dwelling must:</p>
    <ol>
      <li>i) be photoelectric (AS 3786-2014); and</li>
      <li>ii) not also contain an ionisation sensor; and</li>
      <li>iii) be less than 10 years old; and</li>
      <li>iv) operate when tested; and</li>
      <li>v) be interconnected with every other smoke alarm in the dwelling so all activate together.</li>
    </ol>
    <p>Smoke alarms must be installed on each storey:</p>
    <ol>
      <li>i) in each bedroom; and</li>
      <li>ii) in hallways which connect bedrooms and the rest of the dwelling; or</li>
      <li>iii) if there is no hallway, between the bedrooms and other parts of the storey; and</li>
      <li>iv) if there are no bedrooms on a storey at least one smoke alarm must be installed in the most likely path of travel to exit the dwelling.</li>
    </ol>
  </div>
  <div class="abs mid-band"><h2>PRESCRIBED LOCATIONS FOR INSTALLING<br>SMOKE ALARMS</h2></div>
  <div class="abs dark-block dark-block--lower"></div>
  <div class="abs col col-left-low">
    <p>Where practicable smoke alarms must be placed on the ceiling. Smoke alarms must not be placed:</p>
    <ol>
      <li>i) within 300mm of a corner of a ceiling and a wall;</li>
      <li>ii) within 300mm of a light fitting;</li>
      <li>iii) within 400mm of an air-conditioning vent;</li>
      <li>iv) within 400mm of the blades of a ceiling fan.</li>
    </ol>
  </div>
  <div class="abs col col-right-low">
    <p>There are special requirements for stairways, sloping ceilings, and ceilings with exposed beams. Specific requirements will be explained in the Building Fire Safety Regulation 2008.</p>
    <p>If impractical for the prescribed location requirements to be met (e.g. may be affected by steam from shower or fumes from cooking), the owner may put the alarm at another location that will provide a warning to occupants of the dwelling.</p>
  </div>
  <p class="abs closing">New legislation specifies the type, positioning and interconnectedness of alarms, which are critical factors for an early warning and a quick escape. To give your family the best chance of surviving a house fire, update your smoke alarms to match the new legislation as soon as you can.</p>
  <p class="abs call">Call Me on 0418362957</p>
  <div class="abs foot-brand"><span class="brand-name">Tandrell Electrical<br>Electrical Contractor</span></div>
  <div class="abs web-band"><span>www.alarmreadyqld.com</span></div>
</section>

</body>
</html>
```